Larkspur Stillness

Logo picture and I want it to say

yoga. meditation. sound healing

small sweet classes

Larkspur-stillness.com

2740 West Hollander Ave Suite K
Ridgecove ca 90417

```html
<!DOCTYPE html>
<html lang="en">
<head>
<meta charset="utf-8">
<title>Larkspur Stillness — Yoga, Meditation, Sound Healing</title>
<link rel="stylesheet" href="https://fonts.googleapis.com/css2?family=Montserrat:wght@600;700;800&display=swap">
<style>
  :root {
    --page-bg: #f0f0f0;
    --flyer-bg: #000000;
    --ink: #ffffff;
    --orchid: #e8b3d8;
    --rule: #6b6b78;
    --night: #0b0d22;
  }
  * { margin: 0; padding: 0; box-sizing: border-box; }
  html, body {
    width: 783px; height: 1200px; overflow: hidden;
    background: var(--page-bg);
    font-family: "Montserrat", Arial, sans-serif;
  }
  .flyer {
    position: absolute; left: 37px; top: 98px;
    width: 708px; height: 1004px;
    background: var(--flyer-bg);
    box-shadow: 0 2px 8px rgba(0,0,0,0.25);
    overflow: hidden;
    color: var(--ink);
    text-align: center;
  }
  .brand {
    position: absolute; left: 292px; top: 52px;
    width: 124px; height: 124px;
    border: 2px solid var(--ink); border-radius: 50%;
    display: flex; align-items: center; justify-content: center;
  }
  .brand-name {
    font-weight: 600; font-size: 13px; line-height: 1.2;
    color: var(--ink); width: 90px;
  }
  .scene {
    position: absolute; left: 0; top: 440px; width: 708px; height: 520px;
    background:
      radial-gradient(ellipse 16% 40% at 50% 55%, rgba(236,190,225,0.45), transparent 80%),
      radial-gradient(ellipse 38% 48% at 18% 58%, rgba(226,150,212,0.75), transparent 80%),
      radial-gradient(ellipse 38% 50% at 75% 55%, rgba(170,110,225,0.7), transparent 80%),
      radial-gradient(ellipse 80% 60% at 50% 62%, rgba(120,70,180,0.55), transparent 85%),
      linear-gradient(180deg, #000 0%, var(--night) 28%, var(--night) 72%, #000 90%);
  }
  .scene::after {
    content: ""; position: absolute; inset: 0;
    background: linear-gradient(180deg, #000 0%, transparent 22%, transparent 76%, #000 92%);
  }
  .headline { position: absolute; left: 0; top: 196px; width: 100%; font-weight: 800; }
  .headline-yoga { display: block; font-size: 118px; line-height: 118px; color: var(--orchid); letter-spacing: -1px; }
  .headline-meditation { display: block; font-size: 75px; line-height: 74px; margin-top: -2px; letter-spacing: 1px; }
  .headline-sound { display: block; font-size: 56px; line-height: 62px; font-weight: 700; letter-spacing: 1px; }
  .divider { position: absolute; left: 185px; top: 461px; width: 338px; height: 1px; background: var(--rule); }
  .divider-accent { position: absolute; left: 313px; top: 459px; width: 82px; height: 6px; border-radius: 3px; background: var(--orchid); }
  .tagline {
    position: absolute; left: 0; top: 490px; width: 100%;
    font-weight: 700; font-size: 31px; letter-spacing: 0.5px;
  }
  .contact { position: absolute; left: 0; top: 858px; width: 100%; font-weight: 700; font-size: 21px; line-height: 28px; font-style: normal; }
  .contact-line { display: flex; justify-content: center; align-items: flex-start; gap: 10px; }
  .contact-web { margin-top: 14px; align-items: center; }
  .icon { flex: none; margin-top: 3px; }
  .contact-web .icon { margin-top: 0; }
</style>
</head>
<body>
  <main class="flyer">
    <div class="brand"><span class="brand-name">Larkspur Stillness</span></div>

    <div class="scene" role="img" aria-label="Silhouette of a person meditating cross-legged on a hill under a glowing violet and pink starry sky, with coloured chakra dots along the spine"></div>

    <h1 class="headline">
      <span class="headline-yoga">YOGA</span>
      <span class="headline-meditation">MEDITATION</span>
      <span class="headline-sound">SOUND HEALING</span>
    </h1>

    <div class="divider"></div>
    <div class="divider-accent"></div>

    <p class="tagline">SMALL SWEET CLASSES</p>

    <address class="contact">
      <div class="contact-line">
        <svg class="icon" width="16" height="22" viewBox="0 0 16 22" aria-hidden="true">
          <path d="M8 0C3.6 0 0 3.5 0 7.9 0 13.5 8 22 8 22s8-8.5 8-14.1C16 3.5 12.4 0 8 0z" fill="#e8b3d8"/>
          <circle cx="8" cy="8" r="3" fill="#000"/>
        </svg>
        <span>2740 West Hollander Ave Suite K<br>Ridgecove ca 90417</span>
      </div>
      <div class="contact-line contact-web">
        <svg class="icon" width="18" height="18" viewBox="0 0 18 18" aria-hidden="true" fill="none" stroke="#e8b3d8" stroke-width="1.4">
          <circle cx="9" cy="9" r="7.5"/>
          <ellipse cx="9" cy="9" rx="3.3" ry="7.5"/>
          <line x1="1.5" y1="9" x2="16.5" y2="9"/>
          <line x1="2.8" y1="5" x2="15.2" y2="5"/>
          <line x1="2.8" y1="13" x2="15.2" y2="13"/>
        </svg>
        <span>www.larkspur-stillness.com</span>
      </div>
    </address>
  </main>
</body>
</html>
```